Ovaro Letterhead

Need a fresh looking design. We are a IT service company and I would like some elements of the logo to flow through. I have included the logo as an attachment. I have also included business card design as it might help with the design.

Industry/Entity Type

Business

```html
<!DOCTYPE html>
<html lang="en">
<head>
<meta charset="utf-8">
<title>Ovaro Letterhead</title>
<link rel="stylesheet" href="https://fonts.googleapis.com/css2?family=Open+Sans:wght@400;600&display=swap">
<style>
  :root {
    --charcoal: #1e1e1e;
    --lime: #a4cf4c;
    --grey-text: #a3a3a3;
    --slate: #8c979e;
    --paper: #ffffff;
    --mark-tint: #eef0f1;
  }
  * { margin: 0; padding: 0; box-sizing: border-box; }
  html, body { width: 848px; height: 1200px; overflow: hidden; background: var(--paper); }
  body { font-family: "Open Sans", sans-serif; position: relative; }

  .header-shape { position: absolute; top: 0; left: 0; width: 848px; height: 200px; }

  .brand-name {
    position: absolute; left: 34px; top: 24px;
    font-size: 84px; font-weight: 600; letter-spacing: -1px;
    color: var(--lime); line-height: 1;
  }

  .header-contact {
    position: absolute; right: 38px; top: 55px;
    text-align: right; font-size: 14.5px; line-height: 20px;
    color: var(--grey-text); white-space: nowrap;
  }
  .header-contact .label { color: var(--lime); margin-right: 8px; }

  .faint-square {
    position: absolute; left: 275px; top: 450px; width: 300px; height: 300px;
    background: var(--mark-tint); border-radius: 16px;
  }

  .footer-band {
    position: absolute; left: 0; top: 1135px; width: 848px; height: 50px;
    background: var(--charcoal);
    font-size: 12px; color: var(--grey-text);
  }
  .footer-stripe { position: absolute; left: 0; top: 1185px; width: 848px; height: 15px; background: var(--slate); }

  .footer-item {
    position: absolute; top: 0; height: 50px;
    display: flex; align-items: center; gap: 6px; white-space: nowrap;
  }
  .footer-item svg { width: 10px; height: 10px; flex: none; }
  .footer-item .accent { color: var(--lime); }
  .footer-divider { position: absolute; left: 228px; top: 9px; width: 1px; height: 32px; background: var(--grey-text); }

  .item-address { left: 38px; }
  .item-mobile  { left: 246px; }
  .item-phone   { left: 360px; }
  .item-fax     { left: 474px; }
  .item-email   { left: 580px; }
  .item-web     { left: 698px; }
</style>
</head>
<body>
  <svg class="header-shape" viewBox="0 0 848 200" aria-hidden="true">
    <rect x="0" y="0" width="848" height="163" fill="var(--charcoal)"/>
    <path d="M0 163 H470 C505 163 510 193 545 193 H848 V163 Z" fill="var(--lime)"/>
    <rect x="0" y="163" width="470" height="5" fill="var(--lime)"/>
  </svg>

  <div class="brand-name">Ovaro</div>

  <div class="header-contact">
    <div>PO Box 2218, Northbay 2031</div>
    <div><span class="label">Ph:</span>02 9050 4412</div>
    <div><span class="label">Fax:</span>02 9050 4413</div>
  </div>

  <div class="faint-square"></div>

  <footer class="footer-band">
    <div class="footer-item item-address">
      <svg viewBox="0 0 10 10"><circle cx="5" cy="5" r="4" fill="var(--lime)"/></svg>
      <span>PO Box 2218, Northbay 2031</span>
    </div>
    <div class="footer-divider"></div>
    <div class="footer-item item-mobile">
      <svg viewBox="0 0 10 10"><rect x="3" y="1" width="4" height="8" rx="1" fill="none" stroke="var(--lime)" stroke-width="1.2"/></svg>
      <span>0400 555 118</span>
    </div>
    <div class="footer-item item-phone">
      <svg viewBox="0 0 10 10"><path d="M2 1 L4 1 L5 3 L4 4 Q5 6 6 6 L7 5 L9 6 L9 8 Q5 9 2 5 Q1 3 2 1Z" fill="var(--lime)"/></svg>
      <span>02 9050 4412</span>
    </div>
    <div class="footer-item item-fax">
      <svg viewBox="0 0 10 10"><rect x="1" y="3" width="8" height="6" rx="1" fill="var(--lime)"/><rect x="3" y="1" width="4" height="3" fill="var(--lime)"/></svg>
      <span>02 9050 4413</span>
    </div>
    <div class="footer-item item-email">
      <svg viewBox="0 0 10 10"><circle cx="5" cy="5" r="4" fill="none" stroke="var(--lime)" stroke-width="1.4"/></svg>
      <span>mk@ovaro.com.au</span>
    </div>
    <div class="footer-item item-web">
      <svg viewBox="0 0 10 10"><circle cx="5" cy="5" r="4" fill="none" stroke="var(--lime)" stroke-width="1.2"/><path d="M1 5 H9 M5 1 V9" stroke="var(--lime)" stroke-width="1"/></svg>
      <span>www.<span class="accent">ovaro</span>.com.au</span>
    </div>
  </footer>
  <div class="footer-stripe"></div>
</body>
</html>
```